Canvas for our Manager who is an exceptional leader

We need a design that can be printed on a Canvas. We would like to include the words as written below in combination with a Kudu (a deer commonly found in Africa. Please see photo attached as an example of the animal) which will serve as a symbol of leadership. Although it is an African deer, we would prefer if the design is not "Africa themed". We are looking to do a clean, modern design.
Words to be used:

"You inspire greatness in us"

Font styles to use
Other font styles liked:
• Oswald

Requirements
Nice to have
• A cool modern background

```html
<!DOCTYPE html>
<html lang="en">
<head>
<meta charset="utf-8">
<title>You Inspire Greatness In Us</title>
<link rel="stylesheet" href="https://fonts.googleapis.com/css2?family=Oswald:wght@400;700&display=swap">
<style>
  :root {
    --page-bg: #ececec;
    --sun-white: #fffbe0;
    --sun-yellow: #ffe21a;
    --sky-amber: #ffb400;
    --sky-orange: #ff8a12;
    --sky-deep: #f46a0a;
    --ground-dark: #2a0f04;
    --ink: #140803;
    --paper: #ffffff;
  }
  * { margin: 0; padding: 0; box-sizing: border-box; }
  html, body {
    width: 1197px;
    height: 1200px;
    overflow: hidden;
    background: var(--page-bg);
  }
  .poster {
    position: absolute;
    left: 48px;
    top: 201px;
    width: 1100px;
    height: 797px;
    overflow: hidden;
  }
  .poster__scene {
    position: absolute;
    inset: 0;
    background:
      radial-gradient(ellipse 40% 30% at 92% 5%, var(--sun-white) 0%, rgba(255,251,224,0) 70%),
      linear-gradient(to bottom, rgba(42,15,4,0) 0%, rgba(42,15,4,0) 78%, rgba(42,15,4,0.85) 86%, var(--ground-dark) 100%),
      radial-gradient(ellipse 22% 55% at 23% 60%, rgba(42,15,4,0.7) 0%, rgba(42,15,4,0) 70%),
      linear-gradient(160deg, var(--sky-deep) 0%, var(--sky-orange) 30%, var(--sky-amber) 60%, var(--sun-yellow) 100%);
  }
  .poster__message {
    position: absolute;
    left: 452px;
    top: 312px;
    font-family: 'Oswald', sans-serif;
    color: var(--ink);
  }
  .message__lead {
    display: inline-block;
    background: var(--ink);
    color: var(--paper);
    font-weight: 400;
    font-size: 108px;
    line-height: 136px;
    padding: 0 30px 0 14px;
    text-transform: uppercase;
    letter-spacing: -1px;
  }
  .message__tail {
    display: block;
    margin-top: 8px;
    padding-left: 6px;
    line-height: 110px;
    white-space: nowrap;
  }
  .message__key {
    font-weight: 700;
    font-size: 92px;
    text-transform: uppercase;
    letter-spacing: -1px;
  }
  .message__soft {
    font-weight: 400;
    font-size: 62px;
    margin-left: 8px;
  }
</style>
</head>
<body>
  <main class="poster">
    <div class="poster__scene" role="img" aria-label="Photograph of a kudu with spiral horns standing on a grassy ridge, silhouetted against a bright orange and yellow sunset sky"></div>
    <h1 class="poster__message">
      <span class="message__lead">You Inspire</span>
      <span class="message__tail"><span class="message__key">Greatness</span><span class="message__soft">in us</span></span>
    </h1>
  </main>
</body>
</html>
```